Redesign of page from emergency manual

Please redesign this PDF to look better. Please don't include any stock photos. It must be legible. Making some words bold is probably a good idea.

Here are some things I like :

https://tarrowbooks.com.au/collections/frontpage/products/the-plk-v2-ebook

https://img-cd.vostramediafiles.com/qa-ejkwPLOTYY_SuCKbZNu411Qwgjv8YssPxEdzXN93hDkSRjLXK8WmfgbmrJW4ZZ3yUPK=w1052-h592-rw

```html
<!DOCTYPE html>
<html lang="en">
<head>
<meta charset="utf-8">
<title>Hypertension, Acute</title>
<link rel="stylesheet" href="https://fonts.googleapis.com/css2?family=Montserrat:wght@300;400;500;600;700;800&display=swap">
<style>
  :root {
    --brand: #62bbd4;
    --brand-soft: #acdde9;
    --row: #eaf6fa;
    --row-line: #cfe8f0;
    --caution-bg: #f8f6ec;
    --diff-bg: #e9e9ee;
    --ink: #2f3a40;
    --ink-soft: #4a555b;
    --white: #ffffff;
  }
  * { box-sizing: border-box; margin: 0; padding: 0; }
  html, body { width: 801px; height: 1200px; overflow: hidden; background: var(--white); }
  body { font-family: "Montserrat", sans-serif; color: var(--ink); position: relative; }

  .page-header {
    position: absolute; left: 0; top: 0; width: 801px; height: 215px;
    background: var(--brand); color: var(--white); text-align: center;
  }
  .page-title { position: absolute; top: 78px; width: 100%; font-size: 42px; font-weight: 800; letter-spacing: 0.5px; }
  .page-subtitle { position: absolute; top: 137px; width: 100%; font-size: 19px; font-weight: 300; line-height: 25px; }

  .frame { position: absolute; left: 0; top: 0; }

  .intro { position: absolute; top: 238px; width: 100%; text-align: center; font-size: 16.5px; font-weight: 400; line-height: 22px; color: var(--ink-soft); }

  .step { position: absolute; top: 316px; height: 95px; }
  .step-number { position: absolute; top: -6px; font-size: 118px; font-weight: 800; color: var(--brand); line-height: 1; text-shadow: 3px 3px 0 #4aa3bd; }
  .step-card {
    position: absolute; top: 2px; height: 92px; background: var(--brand-soft);
    border-radius: 14px; font-size: 14px; line-height: 17.5px; padding-right: 12px;
    display: flex; align-items: center; color: var(--ink);
  }
  .step-one { left: 64px; width: 320px; }
  .step-one .step-card { left: 34px; width: 282px; padding-left: 20px; }
  .step-two { left: 400px; width: 330px; }
  .step-two .step-card { left: 50px; width: 278px; padding-left: 26px; }

  .bp-table { position: absolute; left: 179px; top: 446px; width: 445px; border-radius: 10px; overflow: hidden; border: 1px solid var(--row-line); }
  .bp-title { height: 30px; background: var(--brand); color: var(--white); font-weight: 600; font-size: 15px; text-align: center; line-height: 30px; }
  .bp-row { display: grid; grid-template-columns: 1fr 1fr 1fr; height: 32px; background: var(--row); border-top: 1px solid var(--row-line); }
  .bp-row span { text-align: center; line-height: 31px; font-size: 13.5px; font-weight: 300; border-left: 1px solid var(--row-line); }
  .bp-row span:first-child { border-left: none; }
  .bp-row.head { background: var(--brand-soft); height: 33px; }
  .bp-row.head span { font-weight: 600; font-size: 14px; border-left-color: #9fd0dd; }

  .caution {
    position: absolute; left: 52px; top: 626px; width: 713px; height: 67px;
    background: var(--caution-bg); border-radius: 8px; padding: 9px 20px;
    font-size: 12.4px; line-height: 16.5px; text-align: justify; color: var(--ink);
  }
  .caution strong { font-weight: 700; }

  .drug-table { position: absolute; left: 97px; top: 706px; width: 625px; border-radius: 12px; overflow: hidden; border: 1px solid var(--row-line); background: var(--row); }
  .drug-row { display: grid; grid-template-columns: 187px 1fr; height: 65px; border-top: 1px solid var(--row-line); }
  .drug-row > div { display: flex; flex-direction: column; justify-content: center; padding: 0 12px; }
  .drug-row .action { border-right: 1px solid var(--row-line); font-size: 10.5px; line-height: 13px; font-weight: 500; }
  .drug-row .drugs { font-size: 10.8px; line-height: 22px; font-weight: 500; }
  .drug-row.head { height: 39px; border-top: none; background: var(--brand); color: var(--white); }
  .drug-row.head > div { font-size: 16px; font-weight: 700; align-items: center; border-right-color: #86cde0; }

  .differential {
    position: absolute; left: 49px; top: 1024px; width: 716px; height: 126px;
    background: var(--diff-bg); border-radius: 14px; padding: 11px 20px;
  }
  .differential h3 { font-size: 13.5px; font-weight: 600; margin-bottom: 10px; }
  .diff-grid { display: grid; grid-template-columns: 283px 226px 1fr; font-size: 13.5px; line-height: 17px; font-weight: 400; color: var(--ink-soft); }
  .diff-col { display: flex; flex-direction: column; }
  .diff-item { display: flex; gap: 10px; align-items: flex-start; }
  .check { flex: none; width: 15px; height: 15px; border: 1.3px solid #b6b8be; border-radius: 3px; margin-top: 1px; background: var(--white); }
  .col-a .diff-item + .diff-item { margin-top: 10px; }
  .col-b .diff-item + .diff-item { margin-top: 6px; }
  .col-c .diff-item + .diff-item { margin-top: 13px; }
</style>
</head>
<body>
  <header class="page-header">
    <h1 class="page-title">HYPERTENSION, ACUTE</h1>
    <p class="page-subtitle">Sustained high blood pressure refractory to<br>treating reversible causes</p>
  </header>

  <svg class="frame" width="801" height="1200" aria-hidden="true">
    <path d="M21 215 V1148 Q21 1160 33 1160 H768 Q780 1160 780 1148 V215" fill="none" stroke="#62bbd4" stroke-width="2.6" stroke-dasharray="9 7"/>
  </svg>

  <p class="intro">In pediatrics, hypertension is almost always treated by addressing likely<br>causes such as light anesthesia or measurement error:</p>

  <section class="step step-one">
    <div class="step-card">Ensure correct BP cuff size: cuff bladder width ~ 40% of limb circumference.</div>
    <span class="step-number" style="left:0">1</span>
  </section>
  <section class="step step-two">
    <div class="step-card">Ensure arterial line transducer is at level of heart<br>(Consider placing arterial line if not already present)</div>
    <span class="step-number" style="left:0">2</span>
  </section>

  <section class="bp-table">
    <div class="bp-title">Hypertensive Blood Pressure Range*</div>
    <div class="bp-row head"><span>Age (Yr)</span><span>Systolic</span><span>Diastolic</span></div>
    <div class="bp-row"><span>New born</span><span>&gt;97</span><span>&gt;70</span></div>
    <div class="bp-row"><span>1 - 3</span><span>&gt;105</span><span>&gt;61</span></div>
    <div class="bp-row"><span>4 - 12</span><span>&gt;113</span><span>&gt;86</span></div>
  </section>

  <p class="caution"><strong>CAUTION</strong>: Anti-hypertensive drugs are almost never needed for routine pediatric cases. These medications are used almost exclusively for specialized cardiac, neurosurgical, or endocrine (pheochromocytoma) cases. Consult an expert before use. Rule-out increased ICP.</p>

  <section class="drug-table">
    <div class="drug-row head"><div class="action">Action</div><div class="drugs">Drug (IV Dosing)</div></div>
    <div class="drug-row">
      <div class="action">Direct smooth muscle<br>relaxation</div>
      <div class="drugs">Sodium nitroprusside 0.5-10 MICROgrams/kg/min<br>HydrALAZINE 0.1-0.2 mg/kg (adult dose 5-10 mg)</div>
    </div>
    <div class="drug-row">
      <div class="action">β-Adrenergic<br>blockade</div>
      <div class="drugs">Esmolol 100-500 MICROgrams/kg over 5 min, then 25-300 MICROgrams/kg/<br>Labetalol (also α effect) 0.2-1 mg/kg q 10 min; 0.4-3 mg/kg/hour (infusion)</div>
    </div>
    <div class="drug-row">
      <div class="action">Calcium channel<br>blockade</div>
      <div class="drugs">niCARdapine 0.5-5 MICROgrams/kg/min<br>Clevidipine 0.5-3.5 MICROgrams/kg/min</div>
    </div>
    <div class="drug-row">
      <div class="action">D1-dopamine agonist</div>
      <div class="drugs">Fenoldopam 0.2-0.8 MICROgrams/kg/min</div>
    </div>
  </section>

  <section class="differential">
    <h3>Consider Differential (Partial):</h3>
    <div class="diff-grid">
      <div class="diff-col col-a">
        <div class="diff-item"><span class="check"></span><span>Light anesthesia (consider vaporizer or infusion pump empty or malfunctioning)</span></div>
        <div class="diff-item"><span class="check"></span><span>Hypercarbia</span></div>
      </div>
      <div class="diff-col col-b">
        <div class="diff-item"><span class="check"></span><span>Hypoxemia</span></div>
        <div class="diff-item"><span class="check"></span><span>Arterial line transducer too low or BP cuff too small</span></div>
        <div class="diff-item"><span class="check"></span><span>Withdrawal (EtOH or opioid)</span></div>
      </div>
      <div class="diff-col col-c">
        <div class="diff-item"><span class="check"></span><span>Thyroid Storm</span></div>
        <div class="diff-item"><span class="check"></span><span>Pheochromocytoma</span></div>
        <div class="diff-item"><span class="check"></span><span>Drug Error</span></div>
      </div>
    </div>
  </section>
</body>
</html>
```